Conservative, Modern and Sharp Builder Business card

Hi there,
We would like to update our existing business card.
I have attached photos of existing business card, logo and van sign.

I would like the business card to also list what we do :
Renovation • New Build • Alteration
Extension • Bathroom • Maintenance.(Seperated by dots)

Contact number : 021 0483 0752
(With that exact spacing)

Ideally when people looking from about 2-3 metres, they know that it is a builder’s business card

Open to suggestions on fonts, layout, style of business card

PLEASE ONLY SUBMIT YOUR BEST OR MAX 3 DESIGNS FOR EACH DESIGNER

Thanks

Industry/Entity Type

Construction. Renovation

Contact Information for Business Card

Details should be the same as the existing card. And addition of what we do.

Requirements
Should not have
• The new business card must not have the same layout as our existing one. Thanks

```html
<!DOCTYPE html>
<html lang="en">
<head>
<meta charset="utf-8">
<title>KeelBuild Business Card</title>
<link href="https://fonts.googleapis.com/css2?family=Montserrat:wght@400;500;600;700&display=swap" rel="stylesheet">
<style>
  :root {
    --navy: #053f76;
    --white: #ffffff;
    --ink: #111111;
    --backdrop: #b3b3b3;
  }
  html, body {
    margin: 0;
    padding: 0;
    width: 1000px;
    height: 1200px;
    overflow: hidden;
    background: var(--backdrop);
    font-family: "Montserrat", sans-serif;
  }
  .card {
    position: absolute;
    left: 51px;
    width: 899px;
    height: 539px;
  }
  .card-front { top: 44px; background: var(--white); }
  .card-back { top: 617px; background: var(--navy); color: var(--white); }

  .brand-name {
    position: absolute;
    margin: 0;
    font-weight: 700;
    line-height: 1;
    letter-spacing: -1px;
  }
  .card-front .brand-name {
    left: 49px;
    top: 205px;
    font-size: 80px;
    color: var(--navy);
  }
  .card-back .brand-name {
    left: 0;
    right: 0;
    top: 320px;
    text-align: center;
    font-size: 80px;
    color: var(--white);
  }

  .contact-block {
    position: absolute;
    left: 510px;
    top: 0;
    color: var(--ink);
  }
  .person-name {
    position: absolute;
    top: 266px;
    margin: 0;
    font-size: 34px;
    font-weight: 600;
    line-height: 1;
    letter-spacing: 1px;
    white-space: nowrap;
  }
  .person-role {
    position: absolute;
    top: 305px;
    margin: 0;
    font-size: 26px;
    font-weight: 400;
    line-height: 1;
    letter-spacing: 0.5px;
    white-space: nowrap;
  }
  .contact-line {
    position: absolute;
    left: 0;
    display: flex;
    align-items: center;
    gap: 8px;
    font-size: 24px;
    line-height: 1;
    white-space: nowrap;
    letter-spacing: 0.3px;
  }
  .contact-icon {
    width: 28px;
    height: 28px;
    flex: none;
  }
  .line-phone { top: 343px; }
  .line-email { top: 386px; }
  .line-web { top: 430px; }
  .line-social { top: 473px; }

  .services {
    position: absolute;
    left: 0;
    right: 0;
    top: 44px;
    margin: 0;
    text-align: center;
    font-size: 31px;
    font-weight: 600;
    line-height: 37px;
    letter-spacing: 1px;
  }
  .phone-callout {
    position: absolute;
    left: 0;
    right: 0;
    top: 463px;
    margin: 0;
    text-align: center;
    font-size: 33px;
    font-weight: 600;
    line-height: 1;
    letter-spacing: 1px;
  }
</style>
</head>
<body>
  <section class="card card-front">
    <p class="brand-name">KeelBuild</p>

    <div class="contact-block">
      <p class="person-name">Dario Menteng</p>
      <p class="person-role">Residential Builder</p>

      <div class="contact-line line-phone">
        <svg class="contact-icon" viewBox="0 0 28 28" aria-hidden="true">
          <rect width="28" height="28" rx="3" fill="var(--navy)"/>
          <path d="M9 6 l3 0 l1.5 4 l-2 1.5 q1.5 3.5 5 5 l1.5 -2 l4 1.5 l0 3 q-1 2 -3 2 q-7 -1 -11 -8 q-1.5 -3.5 1 -7z" fill="var(--white)"/>
        </svg>
        <span>021 0483 0752</span>
      </div>

      <div class="contact-line line-email">
        <svg class="contact-icon" viewBox="0 0 28 28" aria-hidden="true">
          <rect width="28" height="28" rx="3" fill="var(--navy)"/>
          <rect x="6" y="8.5" width="16" height="11" fill="none" stroke="var(--white)" stroke-width="1.6"/>
          <path d="M6 8.5 l8 6 l8 -6 M6 19.5 l6 -5 M22 19.5 l-6 -5" fill="none" stroke="var(--white)" stroke-width="1.4"/>
        </svg>
        <span>KeelBuild@mailbox.com</span>
      </div>

      <div class="contact-line line-web">
        <svg class="contact-icon" viewBox="0 0 28 28" aria-hidden="true">
          <rect width="28" height="28" rx="3" fill="var(--navy)"/>
          <circle cx="14" cy="14" r="8" fill="none" stroke="var(--white)" stroke-width="1.5"/>
          <ellipse cx="14" cy="14" rx="3.5" ry="8" fill="none" stroke="var(--white)" stroke-width="1.3"/>
          <path d="M6 14 h16 M7.5 10 h13 M7.5 18 h13" stroke="var(--white)" stroke-width="1.2"/>
        </svg>
        <span>www. KeelBuild.nz</span>
      </div>

      <div class="contact-line line-social">
        <svg class="contact-icon" viewBox="0 0 28 28" aria-hidden="true">
          <rect width="28" height="28" rx="3" fill="var(--navy)"/>
        </svg>
        <span>KeelBuild.nz</span>
      </div>
    </div>
  </section>

  <section class="card card-back">
    <p class="services">Renovation • New Build • Alteration<br>Extension • Bathroom • Maintenance</p>
    <p class="brand-name">KeelBuild</p>
    <p class="phone-callout">Contact number : 021 0483 0752</p>
  </section>
</body>
</html>
```